6"x9" Postcard Mailer

A 6"x9" Postcard mailer targeted to forensic laboratories to advertise or mock forensic samples (https://veltrasync.example/products/mock-forensic-samples/).

Here is some copy, but we can modify if there is not enough space:

Headline:
Expedite Training, Validation, & R&D with Our Ready-to-Use Mock Samples

Bullet Points:

- Wide Variety of Sample Types: IRB-approved samples mimicking crime scene substances, including semen, hair, bone, saliva, blood, and vaginal epithelial cells.
- Diverse Scenarios: Simulate sexual assault and degraded samples for varied conditions.
- Custom Solutions: Tailored DNA quantities and concentrations to suit your lab's needs.

Use discount code PRAX47 for a 10% discount

```html
<!DOCTYPE html>
<html lang="en">
<head>
<meta charset="utf-8">
<title>Veltrasync Mock Forensic Samples Postcard</title>
<link rel="stylesheet" href="https://fonts.googleapis.com/css2?family=Montserrat:wght@400;500;600;700;800&display=swap">
<style>
  :root {
    --bg: #7d7d7d;
    --blue: #1f5cbf;
    --sky: #2a8fd6;
    --navy: #1b3f9c;
    --ink: #2b2f38;
    --muted: #555b66;
    --paper: #f6f7f9;
    --white: #ffffff;
    --photo-dark: #1e2732;
    --photo-mid: #3a4658;
  }
  * { box-sizing: border-box; margin: 0; padding: 0; }
  html, body { width: 1200px; height: 900px; overflow: hidden; }
  body {
    background: var(--bg);
    font-family: "Montserrat", sans-serif;
    color: var(--ink);
    position: relative;
  }
  .postcard {
    position: absolute;
    width: 560px;
    height: 373px;
    background: var(--paper);
    overflow: hidden;
    box-shadow: 0 10px 24px rgba(0,0,0,.35);
  }
  .postcard--front { left: 27px; top: 263px; }
  .postcard--back { left: 613px; top: 263px; }
  .postcard svg.shapes { position: absolute; inset: 0; }
  .abs { position: absolute; }

  .brand { display: flex; align-items: center; gap: 6px; font-weight: 700; color: var(--navy); }
  .brand__dot { width: 14px; height: 14px; border-radius: 50%; background: var(--navy); }
  .brand__name { font-size: 18px; line-height: 1; }
  .brand__tag { font-size: 7px; font-weight: 500; color: var(--navy); margin-left: 20px; margin-top: 2px; }

  .headline-band {
    left: 0; top: 84px; width: 262px; height: 68px;
    background: var(--sky);
    padding: 8px 10px 0 18px;
    color: var(--white);
    font-weight: 800; font-size: 13.5px; line-height: 1.25;
  }
  .features { left: 16px; top: 162px; width: 262px; list-style: none; }
  .feature { display: flex; gap: 8px; margin-bottom: 6px; font-size: 7.4px; line-height: 1.35; color: var(--muted); }
  .feature__icon {
    flex: 0 0 24px; height: 24px; border-radius: 50%;
    background: var(--blue); border: 2px solid #c9d8f2;
    display: flex; align-items: center; justify-content: center;
  }
  .feature strong { color: var(--blue); font-weight: 700; }

  .discount {
    border: 2px solid var(--sky); border-radius: 6px; overflow: hidden;
    background: var(--white); box-shadow: 0 2px 4px rgba(0,0,0,.15);
  }
  .discount__value {
    background: var(--sky); color: var(--white); white-space: nowrap;
    font-weight: 800; font-size: 20px; line-height: 1; padding: 5px 10px 4px;
  }
  .discount__code { color: var(--ink); font-weight: 700; font-size: 11px; line-height: 1.2; padding: 3px 10px 4px; white-space: nowrap; }

  .contact { color: var(--white); font-size: 10px; font-weight: 500; line-height: 1.55; }
  .contact__row { display: flex; align-items: center; gap: 5px; white-space: nowrap; }
  .contact__row svg { flex: 0 0 10px; }
  .contact__line { display: flex; gap: 14px; }

  .back-title {
    left: 18px; top: 96px;
    background: var(--blue); color: var(--white);
    font-weight: 800; font-size: 11.5px; padding: 4px 10px; letter-spacing: .2px;
  }
  .back-sub { left: 20px; top: 121px; font-weight: 700; font-size: 10px; color: var(--ink); }
  .checklist { left: 20px; top: 139px; list-style: none; font-size: 8.2px; line-height: 1.6; color: var(--ink); font-weight: 500; }
  .checklist li { display: flex; align-items: center; gap: 5px; }
  .tick { width: 9px; height: 9px; border-radius: 50%; background: var(--blue); display: inline-flex; align-items: center; justify-content: center; }

  .indicia {
    right: 26px; top: 14px; width: 70px; height: 44px;
    border: 1px solid #9aa2ad; background: var(--white);
    font-size: 5.6px; font-weight: 700; text-align: center; line-height: 1.3; padding-top: 5px; color: var(--ink);
  }
</style>
</head>
<body>

<section class="postcard postcard--front" aria-label="Postcard front">
  <svg class="shapes" width="560" height="373" viewBox="0 0 560 373">
    <defs>
      <clipPath id="front-photo-clip"><circle cx="510" cy="20" r="250"/></clipPath>
      <linearGradient id="front-photo-grad" x1="0" y1="0" x2="1" y2="1">
        <stop offset="0" stop-color="#20242c"/>
        <stop offset="0.45" stop-color="#2f5fc4"/>
        <stop offset="0.75" stop-color="#c9ccd2"/>
        <stop offset="1" stop-color="#e6e3e3"/>
      </linearGradient>
    </defs>
    <circle cx="510" cy="20" r="263" fill="none" stroke="var(--blue)" stroke-width="6"/>
    <circle cx="510" cy="20" r="255" fill="none" stroke="var(--sky)" stroke-width="3"/>
    <g clip-path="url(#front-photo-clip)" role="img" aria-label="Photo: gloved hands swabbing blood spatter with a sterile swab">
      <rect x="250" y="-240" width="520" height="520" fill="url(#front-photo-grad)"/>
    </g>
    <path d="M0 308 L220 308 Q390 300 560 228 L560 373 L0 373 Z" fill="var(--blue)"/>
    <path d="M220 301 Q390 293 560 220" fill="none" stroke="var(--white)" stroke-width="3"/>
  </svg>

  <div class="abs" style="left:20px; top:24px;">
    <div class="brand"><span class="brand__dot"></span><span class="brand__name">Veltrasync</span></div>
    <div class="brand__tag">Precision in Forensic Science</div>
  </div>

  <h1 class="abs headline-band">Expedite Training, Validation, &amp; R&amp;D with Our Ready-to-Use Mock Samples</h1>

  <ul class="abs features">
    <li class="feature">
      <span class="feature__icon"><svg width="12" height="12" viewBox="0 0 12 12"><path d="M6 1 Q10 6 10 8 A4 4 0 0 1 2 8 Q2 6 6 1Z" fill="none" stroke="#fff" stroke-width="1.3"/></svg></span>
      <p><strong>Wide Variety of Sample Types:</strong> IRB-approved samples mimicking crime scene substances, including semen, hair, bone, saliva, blood, and vaginal epithelial cells.</p>
    </li>
    <li class="feature">
      <span class="feature__icon"><svg width="12" height="12" viewBox="0 0 12 12"><rect x="2" y="2" width="8" height="8" rx="1" fill="none" stroke="#fff" stroke-width="1.3"/><path d="M4 5h4M4 7.5h3" stroke="#fff" stroke-width="1.1"/></svg></span>
      <p><strong>Diverse Scenarios:</strong> Simulate sexual assault and degraded samples for varied conditions.</p>
    </li>
    <li class="feature">
      <span class="feature__icon"><svg width="12" height="12" viewBox="0 0 12 12"><circle cx="6" cy="6" r="2.2" fill="none" stroke="#fff" stroke-width="1.3"/><path d="M6 1v2M6 9v2M1 6h2M9 6h2" stroke="#fff" stroke-width="1.2"/></svg></span>
      <p><strong>Custom Solutions:</strong> Tailored DNA quantities and concentrations to suit your lab's needs.</p>
    </li>
  </ul>

  <div class="abs discount" style="left:110px; top:254px; width:180px;">
    <div class="discount__value">10% DISCOUNT</div>
    <div class="discount__code">Discount Code PRAX47</div>
  </div>

  <div class="abs contact" style="left:16px; top:318px;">
    <div class="contact__line">
      <span class="contact__row"><svg width="10" height="10" viewBox="0 0 10 10"><circle cx="5" cy="5" r="4.3" fill="none" stroke="#fff" stroke-width="1"/><path d="M3.4 3 L4.2 2.8 L4.6 4 L4 4.4 Q4.6 5.6 5.6 6 L6 5.4 L7.2 5.8 L7 6.6 Q5 7 3.4 3Z" fill="#fff"/></svg>5550 142 290</span>
      <span class="contact__row"><svg width="10" height="10" viewBox="0 0 10 10"><circle cx="5" cy="5" r="4.3" fill="none" stroke="#fff" stroke-width="1"/><rect x="2.8" y="3.4" width="4.4" height="3.2" fill="none" stroke="#fff" stroke-width=".8"/><path d="M2.8 3.4 L5 5.2 L7.2 3.4" fill="none" stroke="#fff" stroke-width=".8"/></svg>info@veltrasync.example</span>
    </div>
    <span class="contact__row"><svg width="10" height="10" viewBox="0 0 10 10"><circle cx="5" cy="5" r="4.3" fill="none" stroke="#fff" stroke-width="1"/><ellipse cx="5" cy="5" rx="1.8" ry="4.3" fill="none" stroke="#fff" stroke-width=".7"/><path d="M.7 5h8.6" stroke="#fff" stroke-width=".7"/></svg>www.veltrasync.example</span>
  </div>
</section>

<section class="postcard postcard--back" aria-label="Postcard back">
  <svg class="shapes" width="560" height="373" viewBox="0 0 560 373">
    <defs>
      <linearGradient id="back-photo-grad" x1="0" y1="0" x2="1" y2="1">
        <stop offset="0" stop-color="var(--photo-mid)"/>
        <stop offset="1" stop-color="var(--photo-dark)"/>
      </linearGradient>
    </defs>
    <g role="img" aria-label="Photo: two white and blue sample kit boxes, one open showing vials">
      <path d="M0 222 L330 186 Q350 250 368 300 L0 340 Z" fill="url(#back-photo-grad)"/>
    </g>
    <path d="M270 76 Q345 84 368 190 Q392 306 560 316" fill="none" stroke="var(--sky)" stroke-width="4"/>
    <path d="M282 84 Q352 96 376 200 Q400 300 560 308" fill="none" stroke="var(--blue)" stroke-width="2"/>
    <path d="M0 320 L250 320 Q390 312 560 316 L560 373 L0 373 Z" fill="var(--blue)"/>
    <g stroke="#b8bec8" stroke-width="1">
      <line x1="400" y1="150" x2="530" y2="150"/>
      <line x1="410" y1="185" x2="535" y2="185"/>
      <line x1="425" y1="220" x2="540" y2="220"/>
    </g>
  </svg>

  <div class="abs" style="left:336px; top:62px;">
    <div class="brand"><span class="brand__dot"></span><span class="brand__name" style="font-size:15px;">Veltrasync</span></div>
    <div class="brand__tag" style="font-size:6px;">Precision in Forensic Science</div>
  </div>

  <div class="abs indicia">PRSRT STD<br>ECRWSS<br>U.S.POSTAGE<br>PAID<br>EDDM Retail</div>

  <h2 class="abs back-title">MOCK FORENSIC SAMPLES</h2>
  <p class="abs back-sub">Realistic mock samples simulating forensic scenarios</p>
  <ul class="abs checklist">
    <li><span class="tick"><svg width="6" height="6" viewBox="0 0 6 6"><path d="M1 3 L2.5 4.5 L5 1.5" fill="none" stroke="#fff" stroke-width="1.1"/></svg></span>Varying DNA sources such as semen, blood, and saliva</li>
    <li><span class="tick"><svg width="6" height="6" viewBox="0 0 6 6"><path d="M1 3 L2.5 4.5 L5 1.5" fill="none" stroke="#fff" stroke-width="1.1"/></svg></span>Includes challenging 2 and 3-person donor mixtures</li>
    <li><span class="tick"><svg width="6" height="6" viewBox="0 0 6 6"><path d="M1 3 L2.5 4.5 L5 1.5" fill="none" stroke="#fff" stroke-width="1.1"/></svg></span>Ideal for training, competency testing, validation and R&amp;D studies</li>
    <li><span class="tick"><svg width="6" height="6" viewBox="0 0 6 6"><path d="M1 3 L2.5 4.5 L5 1.5" fill="none" stroke="#fff" stroke-width="1.1"/></svg></span>Customizable options to suit your laboratory's needs</li>
  </ul>

  <div class="abs discount" style="left:112px; top:216px; width:180px;">
    <div class="discount__value">10% DISCOUNT</div>
    <div class="discount__code">Discount Code PRAX47</div>
  </div>

  <div class="abs contact" style="left:16px; top:330px;">
    <div class="contact__line">
      <span class="contact__row"><svg width="10" height="10" viewBox="0 0 10 10"><circle cx="5" cy="5" r="4.3" fill="none" stroke="#fff" stroke-width="1"/><path d="M3.4 3 L4.2 2.8 L4.6 4 L4 4.4 Q4.6 5.6 5.6 6 L6 5.4 L7.2 5.8 L7 6.6 Q5 7 3.4 3Z" fill="#fff"/></svg>5550 142 290</span>
      <span class="contact__row"><svg width="10" height="10" viewBox="0 0 10 10"><circle cx="5" cy="5" r="4.3" fill="none" stroke="#fff" stroke-width="1"/><rect x="2.8" y="3.4" width="4.4" height="3.2" fill="none" stroke="#fff" stroke-width=".8"/><path d="M2.8 3.4 L5 5.2 L7.2 3.4" fill="none" stroke="#fff" stroke-width=".8"/></svg>info@veltrasync.example</span>
    </div>
    <span class="contact__row"><svg width="10" height="10" viewBox="0 0 10 10"><circle cx="5" cy="5" r="4.3" fill="none" stroke="#fff" stroke-width="1"/><ellipse cx="5" cy="5" rx="1.8" ry="4.3" fill="none" stroke="#fff" stroke-width=".7"/><path d="M.7 5h8.6" stroke="#fff" stroke-width=".7"/></svg>www.veltrasync.example</span>
  </div>
</section>

</body>
</html>
```